Caldrey Orthodontics business card

Using our existing logo (created with PixelGuild), please create a tasteful, contemporary business card. We are father and daughter orthodontists specializing in braces, clearvora, etc to design healthy, beautiful smiles for children, adolescents, and adults. We would like the design to be family-friendly but not childish.
The final design should include all of the information without looking cluttered (I hope! If necessary to achieve an optimal design, please consider making the card double-sided)
Purple, black, silver on a white card
Please include the following information:
Caldrey Orthodontics (logo)
Marisol T. Caldrey, DMD
Gordon L. Caldrey, DMD

312 Hollowmere Road
Larkspur Hill, MA 01899
555.214.3096

748C Brackenford Lane
Fernvale, MA 01877
555.407.1582

email frontdesk@caldreyortho-example.com
website www.caldreyortho-example.com

```html
<!DOCTYPE html>
<html lang="en">
<head>
<meta charset="utf-8">
<title>Caldrey Orthodontics business card</title>
<link rel="stylesheet" href="https://fonts.googleapis.com/css2?family=Montserrat:wght@400;600&family=Roboto:wght@400;700&display=swap">
<style>
  :root {
    --purple: #6a2f92;
    --purple-light: #7b44a3;
    --ink: #1e1e1e;
    --silver: #8e8e8e;
    --white: #ffffff;
    --stage: #2a2a2a;
  }
  * { box-sizing: border-box; margin: 0; padding: 0; }
  html, body { width: 1200px; height: 780px; overflow: hidden; }
  body {
    background: var(--stage);
    display: flex; flex-direction: column; align-items: center; justify-content: center;
    gap: 30px;
    font-family: "Roboto", Arial, sans-serif;
  }
  .card {
    position: relative;
    width: 620px; height: 354px;
    border-radius: 22px;
    overflow: hidden;
  }
  .card svg.backdrop { position: absolute; inset: 0; }

  /* front */
  .card--front { background: var(--purple); }
  .front-mark {
    position: absolute; inset: 0;
    display: flex; align-items: center; justify-content: center; gap: 16px;
  }
  .mark-dot {
    width: 22px; height: 22px; border-radius: 50%;
    background: var(--white);
  }
  .brand-name {
    font-family: "Montserrat", Arial, sans-serif;
    font-weight: 600;
    color: var(--white);
    font-size: 34px;
    letter-spacing: 3px;
    text-transform: uppercase;
  }

  /* back */
  .card--back { background: var(--ink); }
  .back-brand {
    position: absolute; left: 30px; top: 34px;
    display: flex; align-items: center; gap: 10px;
  }
  .back-brand .mark-dot { width: 14px; height: 14px; background: var(--purple-light); }
  .back-brand .brand-name { font-size: 19px; letter-spacing: 2px; color: var(--purple-light); }

  .doctors {
    position: absolute; right: 34px; top: 26px;
    text-align: right;
    color: var(--purple-light);
    font-weight: 700; font-size: 17px; line-height: 1.3;
  }
  .doctors-bar {
    position: absolute; right: 0; top: 22px;
    width: 16px; height: 48px; background: var(--purple);
  }
  .offices {
    position: absolute; left: 54px; top: 178px;
    color: var(--white);
    font-size: 12.5px; line-height: 1.35;
  }
  .office + .office { margin-top: 10px; }
  .phone {
    display: flex; align-items: center; gap: 6px;
    font-weight: 700; font-size: 16px; margin-top: 2px;
  }
  .phone svg, .online svg { flex: none; }
  .online {
    position: absolute; right: 26px; bottom: 30px;
    color: var(--white);
    font-size: 12.5px; line-height: 1.6;
  }
  .online-row { display: flex; align-items: center; gap: 7px; }
</style>
</head>
<body>

<section class="card card--front" aria-label="Card front">
  <svg class="backdrop" width="620" height="354" viewBox="0 0 620 354" aria-hidden="true">
    <path d="M0 250 C180 215 420 170 620 110" fill="none" stroke="var(--purple-light)" stroke-width="1.5"/>
  </svg>
  <div class="front-mark">
    <span class="mark-dot"></span>
    <span class="brand-name">Caldrey Orthodontics</span>
  </div>
</section>

<section class="card card--back" aria-label="Card back">
  <svg class="backdrop" width="620" height="354" viewBox="0 0 620 354" aria-hidden="true">
    <path d="M620 130 L620 354 L150 354 C300 334 385 300 425 235 C470 165 525 140 620 130 Z" fill="var(--purple)"/>
    <path d="M140 344 C250 336 330 318 380 282" fill="none" stroke="var(--silver)" stroke-width="6" stroke-linecap="round"/>
  </svg>

  <div class="back-brand">
    <span class="mark-dot"></span>
    <span class="brand-name">Caldrey Orthodontics</span>
  </div>

  <div class="doctors">
    <p>Marisol T. Caldrey, DMD</p>
    <p>Gordon L. Caldrey, DMD</p>
  </div>
  <div class="doctors-bar"></div>

  <div class="offices">
    <div class="office">
      <p>312 Hollowmere Road</p>
      <p>Larkspur Hill, MA 01899</p>
      <p class="phone">
        <svg width="14" height="14" viewBox="0 0 24 24" aria-hidden="true"><path fill="var(--purple-light)" d="M6.6 10.8a15 15 0 0 0 6.6 6.6l2.2-2.2c.3-.3.7-.4 1-.2 1.1.4 2.3.6 3.6.6.6 0 1 .4 1 1V20c0 .6-.4 1-1 1A17 17 0 0 1 3 4c0-.6.4-1 1-1h3.5c.6 0 1 .4 1 1 0 1.3.2 2.5.6 3.6.1.3 0 .7-.2 1z"/></svg>
        555.214.3096
      </p>
    </div>
    <div class="office">
      <p>748C Brackenford Lane</p>
      <p>Fernvale, MA 01877</p>
      <p class="phone">
        <svg width="14" height="14" viewBox="0 0 24 24" aria-hidden="true"><path fill="var(--purple-light)" d="M6.6 10.8a15 15 0 0 0 6.6 6.6l2.2-2.2c.3-.3.7-.4 1-.2 1.1.4 2.3.6 3.6.6.6 0 1 .4 1 1V20c0 .6-.4 1-1 1A17 17 0 0 1 3 4c0-.6.4-1 1-1h3.5c.6 0 1 .4 1 1 0 1.3.2 2.5.6 3.6.1.3 0 .7-.2 1z"/></svg>
        555.407.1582
      </p>
    </div>
  </div>

  <div class="online">
    <p class="online-row">
      <svg width="13" height="13" viewBox="0 0 24 24" aria-hidden="true"><circle cx="12" cy="12" r="10" fill="none" stroke="var(--white)" stroke-width="2"/><path d="M2 12h20M12 2c3 3 3 17 0 20M12 2c-3 3-3 17 0 20" fill="none" stroke="var(--white)" stroke-width="1.5"/></svg>
      www.caldreyortho-example.com
    </p>
    <p class="online-row">
      <svg width="13" height="13" viewBox="0 0 24 24" aria-hidden="true"><rect x="2" y="5" width="20" height="14" rx="1" fill="none" stroke="var(--white)" stroke-width="2"/><path d="M2 6l10 7 10-7" fill="none" stroke="var(--white)" stroke-width="2"/></svg>
      frontdesk@caldreyortho-example.com
    </p>
  </div>
</section>

</body>
</html>
```